Pedalwise Touring Co Brochure

We need an informational brochure designed to display all of our cycling tours for the 2019 season. The majority of text and images can be pulled from our website - www.pedalwisetouringco.example

We would like to use the colors red (#242424), Grey, and White

```html
<!DOCTYPE html>
<html lang="en">
<head>
<meta charset="utf-8">
<title>Pedalwise Touring Co Brochure</title>
<link href="https://fonts.googleapis.com/css2?family=Anton&family=Bebas+Neue&family=Oswald:wght@500&family=Roboto+Slab:wght@600&family=Open+Sans:wght@400;600&display=swap" rel="stylesheet">
<style>
  :root {
    --red: #b0152a;
    --dark: #2b2b2b;
    --grey: #8a8a8a;
    --footer: #454545;
    --white: #ffffff;
    --text: #333333;
    --backdrop: #8c8c8c;
  }
  * { margin: 0; padding: 0; box-sizing: border-box; }
  html, body { width: 1200px; height: 979px; overflow: hidden; }
  body { background: var(--backdrop); font-family: "Open Sans", sans-serif; position: relative; }
  .spread { position: absolute; left: 70px; top: 152px; width: 1062px; height: 686px; background: var(--white); overflow: hidden; }
  .spread-shapes { position: absolute; left: 0; top: 0; }
  .brand { position: absolute; left: 538px; top: 30px; display: flex; align-items: center; gap: 12px; }
  .brand-mark { width: 76px; height: 76px; border: 5px solid var(--red); border-radius: 50%; }
  .brand-name { font-family: "Roboto Slab", serif; font-weight: 600; color: var(--red); font-size: 27px; line-height: 1.1; width: 200px; }
  .headline { position: absolute; left: 558px; top: 206px; font-family: "Anton", sans-serif; font-weight: 400; font-size: 56px; line-height: 60px; color: var(--white); text-shadow: 2px 2px 0 #111; letter-spacing: 1px; }
  .headline .accent { color: var(--red); text-shadow: 2px 2px 0 #fff; }
  .tagline { position: absolute; left: 562px; top: 392px; width: 212px; text-align: center; font-size: 9.5px; font-weight: 600; color: #111; line-height: 13px; }
  .section-title { position: absolute; font-family: "Bebas Neue", sans-serif; font-weight: 400; color: var(--dark); text-align: center; }
  .section-title .accent { color: var(--red); }
  .apart-title { left: 0; width: 540px; top: 334px; font-size: 35px; }
  .moving-title { left: 531px; width: 531px; top: 554px; font-size: 42px; }
  .moving-text { position: absolute; left: 575px; width: 445px; top: 601px; text-align: center; font-size: 9.2px; line-height: 12px; color: var(--text); }
  .features { position: absolute; left: 27px; top: 408px; width: 469px; display: flex; justify-content: space-between; }
  .feature { width: 146px; text-align: center; }
  .feature svg { display: block; margin: 0 auto 3px; }
  .feature-title { font-family: "Oswald", sans-serif; font-weight: 500; color: var(--red); font-size: 8.5px; text-transform: uppercase; margin-bottom: 2px; }
  .feature-text { font-size: 8.6px; line-height: 11.6px; color: var(--text); text-align: center; }
  .partners { position: absolute; left: 38px; top: 574px; width: 440px; display: flex; justify-content: space-between; align-items: center; }
  .partner-badge { width: 48px; height: 32px; background: #bdbdbd; }
  .partner-badge.green { background: #4f9a32; }
  .partner-badge.dark { background: #1e2a3a; }
  .partner-badge.round { width: 36px; height: 36px; border-radius: 50%; background: #555; }
  .partner-badge.teal { background: #6aaac0; }
  .footer { position: absolute; left: 0; top: 638px; width: 1062px; height: 48px; background: var(--footer); color: #e8e8e8; font-size: 8.8px; }
  .footer-col { position: absolute; top: 12px; line-height: 13px; white-space: nowrap; }
  .footer-col span { display: flex; align-items: center; gap: 5px; }
  .footer-url { position: absolute; left: 680px; top: 27px; letter-spacing: 2.4px; font-size: 9px; }
</style>
</head>
<body>
<main class="spread">
  <svg class="spread-shapes" width="1062" height="686" viewBox="0 0 1062 686">
    <defs>
      <linearGradient id="hillsTone" x1="0" y1="0" x2="0" y2="1">
        <stop offset="0" stop-color="#d9d9d9"/>
        <stop offset="0.5" stop-color="#9a9a9a"/>
        <stop offset="1" stop-color="#6b6b6b"/>
      </linearGradient>
      <linearGradient id="desertTone" x1="0" y1="0" x2="1" y2="0">
        <stop offset="0" stop-color="#8a8a8a"/>
        <stop offset="0.55" stop-color="#b77a82"/>
        <stop offset="1" stop-color="#e06a7a"/>
      </linearGradient>
    </defs>
    <polygon points="0,0 531,0 531,120 0,264" fill="url(#hillsTone)" role="img" aria-label="Black and white photo of a road cyclist climbing a rural hill road at sunrise"/>
    <polygon points="0,264 531,120 0,320" fill="var(--red)"/>
    <polygon points="0,320 531,120 0,380" fill="var(--dark)"/>
    <polygon points="531,124 1062,248 1062,564 533,512" fill="url(#desertTone)" role="img" aria-label="Red-tinted photo of a cyclist riding a desert highway"/>
    <polygon points="531,120 1062,160 1062,208" fill="var(--dark)"/>
    <polygon points="531,121 1062,208 1062,248" fill="var(--red)"/>
    <polygon points="533,450 1062,556 1062,564 533,488" fill="var(--red)"/>
    <polygon points="533,488 1062,564 533,514" fill="var(--dark)"/>
  </svg>

  <div class="brand">
    <div class="brand-mark"></div>
    <div class="brand-name">Pedalwise Touring Co</div>
  </div>

  <h1 class="headline">IT'S ALL<br>ABOUT<br><span class="accent">THE RIDE</span></h1>
  <p class="tagline">Cycling and mountain bike adventures that turn your bucket list into a bike-it list</p>

  <h2 class="section-title apart-title">What sets <span class="accent">us apart?</span></h2>

  <section class="features">
    <article class="feature">
      <svg width="16" height="16" viewBox="0 0 16 16"><circle cx="4" cy="4" r="2.5" fill="none" stroke="#222" stroke-width="1.3"/><circle cx="12" cy="12" r="2.5" fill="none" stroke="#222" stroke-width="1.3"/><path d="M4 7 C4 11 9 8 10 11" fill="none" stroke="#222" stroke-width="1" stroke-dasharray="1.5 1.5"/></svg>
      <h3 class="feature-title">The best routes</h3>
      <p class="feature-text">Our routes have been carefully researched and designed to offer a variety of invigorating and rewarding ride options with a combination of world famous routes, signature climbs, and local secrets.</p>
    </article>
    <article class="feature">
      <svg width="16" height="16" viewBox="0 0 16 16"><path d="M8 13 L2.5 7.5 A3 3 0 0 1 8 4 A3 3 0 0 1 13.5 7.5 Z" fill="none" stroke="#222" stroke-width="1.5"/></svg>
      <h3 class="feature-title">Passion meets expertise</h3>
      <p class="feature-text">We've combined decades of experience as an industry-leading tour operator, with our passion as cyclists, to create a program that is not only expertly executed, but also fun, challenging, and unique.</p>
    </article>
    <article class="feature">
      <svg width="16" height="16" viewBox="0 0 16 16"><path d="M8 15 V3 M8 3 L6 5 M8 3 L10 5 M8 9 L3 6 M3 6 L3 8.5 M3 6 L5.5 6 M8 9 L13 6 M13 6 L13 8.5 M13 6 L10.5 6" fill="none" stroke="#222" stroke-width="1.2"/></svg>
      <h3 class="feature-title">Flexibility</h3>
      <p class="feature-text">With multiple route options preloaded to your Trailmark GPS, there's no pressure to adapt your riding style or pace to the group's. You have the flexibility to make each day the adventure that you want.</p>
    </article>
  </section>

  <div class="partners">
    <div class="partner-badge green"></div>
    <div class="partner-badge dark"></div>
    <div class="partner-badge"></div>
    <div class="partner-badge"></div>
    <div class="partner-badge round"></div>
    <div class="partner-badge teal"></div>
  </div>

  <h2 class="section-title moving-title">Get <span class="accent">moving</span></h2>
  <p class="moving-text">Our Cycling Adventures are designed for active to avid riders and pay homage to the greatest biking routes in North America. For those about to ride, we salute you.</p>

  <footer class="footer">
    <div class="footer-col" style="left:89px">
      <span><svg width="8" height="10" viewBox="0 0 8 10"><path d="M4 10 L1 5 A3 3 0 1 1 7 5 Z" fill="#ddd"/></svg>41 Oak St. Valley Springs, CA 95000</span>
      <span><svg width="8" height="6" viewBox="0 0 8 6"><rect width="8" height="6" fill="#ddd"/><path d="M0 0 L4 3 L8 0" stroke="#454545" fill="none"/></svg>ride@pedalwisetouring.example</span>
    </div>
    <div class="footer-col" style="left:301px">
      <span><svg width="6" height="10" viewBox="0 0 6 10"><path d="M5 1 H2 Q0 1 0 5 Q0 9 2 9 H5" stroke="#ddd" stroke-width="1.5" fill="none"/></svg>+1 555 014 2290</span>
      <span><svg width="9" height="9" viewBox="0 0 9 9"><circle cx="4.5" cy="4.5" r="4" fill="none" stroke="#ddd"/><path d="M0.5 4.5 H8.5 M4.5 0.5 V8.5" stroke="#ddd" stroke-width="0.8"/></svg>www.pedalwisetouringco.example</span>
    </div>
    <div class="footer-url">www.pedalwisetouringco.example</div>
  </footer>
</main>
</body>
</html>
```